Packaging design for HOT NEW RETAIL BEARD OIL BRAND - Merrow Fennick Apothecary

Packaging design for beard oils. I've attached a brief, and I've also attached a few examples of bottles and boxes. Of course, we need an entirely unique look. I've attached the photo of Merrow Fennick as well - you can choose to use it or not (I'm open).

This product will be sold at national retailers and needs to look like a brand that is sold at boutique

What the consumer wants to see on the shelf:
-Box should larger than others and be soft touch (feels luxurious)
-More “hipster look/feel”
-Text should stand out like inspiration photos - jumping off the shelf to the consumer
-Use the existing logo of Merrow Fennick
-Deco will be wrap label as shown in current product image
-Sample text to pull copy for outer carton (taken from label on glass bottle):
-Strengthen and condition your beard with this blend of natural oils. Sunflower oil is rich in omega, fatty acids and vitamins E, C, B, and A, while avocado oil hydrates the beard fibers from root to tip, keep the beard looking and feeling extraordinary. Smooth into your beard for a healthy sheen and a woodsy scent evoking the great outdoors.
-Cool/Hipster product at discount pricing

Target Market(s)

Men from ages 20-40. Women also buy this product for their men, so it needs to look like a well known brand.

Industry/Entity Type

Hair And Beauty

Font styles to use
Sans Serif

Colors

Designer to choose colors to be used in the design.

Requirements
Must have
• A full label and box design with key call outs:
• Features and benefits - found in attached brief
• Description of what it is: Beard Oil
• Name of frangrance: Sandalwood
• Size: 2 oz / 60 ml
Nice to have
• Feel free to revamp the logo if needed. I am not married to the font for Merrow Fennick Apothecary.

```html
<!DOCTYPE html>
<html lang="en">
<head>
<meta charset="utf-8">
<title>Merrow Fennick Apothecary – Beard Oil Wrap Label</title>
<link href="https://fonts.googleapis.com/css2?family=Archivo+Black&family=Open+Sans:wght@300;400;600;700&family=Gochi+Hand&display=swap" rel="stylesheet">
<style>
  :root {
    --ink: #000000;
    --paper: #ffffff;
    --gold: #b07e02;
    --photo-dark: #2b2b2b;
    --photo-light: #bdbdbd;
  }
  * { margin: 0; padding: 0; box-sizing: border-box; }
  html, body { width: 1200px; height: 1000px; overflow: hidden; background: var(--paper); }
  .canvas { position: relative; width: 1200px; height: 1000px; background: var(--paper); font-family: "Open Sans", Arial, sans-serif; }

  /* top flap with fragrance name */
  .flap { position: absolute; left: 866px; top: 127px; width: 271px; height: 270px; background: var(--ink); }
  .flap-band { position: absolute; left: 0; top: 135px; width: 100%; height: 135px; background: var(--gold); }
  .fragrance { position: absolute; left: 0; top: 98px; width: 100%; transform: rotate(180deg); text-align: center;
    font-family: "Open Sans", Arial, sans-serif; font-weight: 400; font-size: 34px; letter-spacing: 6px; line-height: 37px; }
  .fragrance .line-top { display: block; color: var(--ink); }
  .fragrance .line-bottom { display: block; color: var(--gold); }

  /* main wrap band */
  .wrap-band { position: absolute; left: 57px; top: 397px; width: 1080px; height: 470px; background: var(--ink); }

  .portrait { position: absolute; left: 269px; top: 0; width: 271px; height: 258px;
    background: linear-gradient(135deg, var(--photo-light) 0%, #7a7a7a 45%, var(--photo-dark) 100%); }
  .brand-plate { position: absolute; left: 269px; top: 258px; width: 271px; height: 143px; background: var(--gold);
    display: flex; flex-direction: column; align-items: center; justify-content: center; color: var(--ink);
    font-family: "Open Sans", Arial, sans-serif; font-weight: 700; text-align: center; }
  .brand-name { font-size: 28px; line-height: 32px; letter-spacing: 1px; text-transform: uppercase; }
  .brand-sub { font-size: 12px; letter-spacing: 2px; text-transform: uppercase; margin-top: 10px; }
  .product-name { position: absolute; left: 269px; top: 418px; width: 271px; text-align: center; color: var(--paper);
    font-weight: 700; font-size: 30px; }

  /* price tag */
  .price-tag { position: absolute; left: 992px; top: 0; width: 63px; height: 115px; }
  .price-text { position: absolute; left: 992px; top: 22px; width: 63px; text-align: center; color: var(--paper); }
  .price-label { font-size: 15px; font-weight: 400; display: block; }
  .price-value { font-size: 28px; font-weight: 400; line-height: 30px; }
  .price-value sup { font-size: 11px; vertical-align: 13px; }
  .price-value .currency { font-size: 18px; }

  .pitch { position: absolute; left: 829px; top: 56px; color: var(--paper); font-size: 18px; line-height: 23px; }
  .pitch strong { font-family: "Archivo Black", Arial, sans-serif; font-weight: 400; font-size: 16px; letter-spacing: 0.5px; }

  /* benefits panel */
  .benefits { position: absolute; left: 828px; top: 150px; width: 232px; height: 296px; border: 2px solid var(--gold);
    color: var(--paper); padding: 18px 14px 0 16px; }
  .benefit-heavy { font-family: "Archivo Black", Arial, sans-serif; font-size: 20px; line-height: 27px; letter-spacing: 0.5px; white-space: nowrap; }
  .rule { height: 2px; background: var(--paper); margin: 2px 0; }
  .benefit-light { font-weight: 400; font-size: 24px; line-height: 29px; letter-spacing: 2.5px; white-space: nowrap; }
  .benefit-spaced { font-family: "Archivo Black", Arial, sans-serif; font-size: 17px; line-height: 22px; letter-spacing: 9.5px; }
  .benefit-big { font-family: "Archivo Black", Arial, sans-serif; font-size: 49px; line-height: 48px; letter-spacing: -1px; }
  .benefit-script { font-family: "Gochi Hand", cursive; font-size: 24px; line-height: 30px; letter-spacing: 2px; }
  .size { text-align: center; font-size: 16px; margin-top: 18px; letter-spacing: 0.5px; }
</style>
</head>
<body>
<div class="canvas">
  <div class="flap">
    <div class="flap-band"></div>
    <div class="fragrance"><span class="line-top">SANDAL</span><span class="line-bottom">WOOD</span></div>
  </div>

  <div class="wrap-band">
    <div class="portrait" role="img" aria-label="Black-and-white portrait of the bearded brand namesake"></div>
    <div class="brand-plate">
      <span class="brand-name">Merrow<br>Fennick</span>
      <span class="brand-sub">Apothecary</span>
    </div>
    <div class="product-name">BEARD OIL</div>

    <svg class="price-tag" viewBox="0 0 63 115" aria-hidden="true">
      <polygon points="0,0 63,0 63,89 32,115 0,89" fill="var(--gold)"/>
    </svg>
    <div class="price-text">
      <span class="price-label">Retail</span>
      <span class="price-value"><span class="currency">$</span>5<sup>.99</sup></span>
    </div>

    <div class="pitch"><strong>COOL/HIPSTER</strong><br>PRODUCT AT<br>DISCOUNT PRICING</div>

    <div class="benefits">
      <div class="benefit-heavy">STRENGTHEN</div>
      <div class="benefit-heavy">&amp; CONDITION</div>
      <div class="rule"></div>
      <div class="benefit-light">HYDRATES</div>
      <div class="benefit-light">THE BEARD</div>
      <div class="rule"></div>
      <div class="benefit-spaced">HEALTHY</div>
      <div class="benefit-big">SHEEN</div>
      <div class="rule"></div>
      <div class="benefit-script">woodsy scent</div>
      <div class="size">60ml 2 fl. oz.</div>
    </div>
  </div>
</div>
</body>
</html>
```